M Zyvantics Buisness Cards

I need a technology focused clean business card for my employees. I have attached out logo to include in the mocks. We're a modern tech consulting firm that drives to interface humanity with technology in a truly cohesive fashion.

```html
<!DOCTYPE html>
<html lang="en">
<head>
<meta charset="utf-8">
<title>M Zyvantics — Business Card</title>
<link rel="stylesheet" href="https://fonts.googleapis.com/css2?family=Exo+2:wght@200;600&display=swap">
<style>
  :root {
    --ink-dark: #333333;
    --paper: #ffffff;
    --text-grey: #8a8b8e;
    --rule-grey: #a9a9ab;
    --band-grey: #d1d2d4;
    --accent-teal: #33b6c6;
    --accent-blue: #1e78c2;
  }
  html, body {
    margin: 0;
    width: 1200px;
    height: 750px;
    overflow: hidden;
    background: var(--paper);
  }
  .card {
    position: relative;
    width: 1200px;
    height: 750px;
    font-family: "Exo 2", sans-serif;
  }
  .card-face {
    position: absolute;
    left: 15px;
    top: 13px;
    width: 1169px;
    height: 726px;
    border-radius: 12px;
    overflow: hidden;
    background: var(--paper);
  }
  .header-band {
    position: absolute;
    left: 0;
    top: 0;
    width: 100%;
    height: 282px;
    background: var(--ink-dark);
  }
  .brand-panel {
    position: absolute;
    left: 50px;
    top: 38px;
    width: 763px;
    height: 260px;
    background: var(--paper);
    border-radius: 12px 12px 0 0;
    display: flex;
    align-items: center;
    gap: 34px;
    padding-left: 35px;
    box-sizing: border-box;
  }
  .brand-dot {
    width: 150px;
    height: 150px;
    border-radius: 50%;
    background: var(--accent-blue);
    flex: none;
  }
  .brand-name {
    font-weight: 600;
    font-size: 82px;
    color: var(--text-grey);
    letter-spacing: 1px;
    white-space: nowrap;
  }
  .rule-vertical {
    position: absolute;
    left: 1092px;
    top: 0;
    width: 3px;
    height: 644px;
    background: var(--rule-grey);
  }
  .rule-horizontal {
    position: absolute;
    left: 813px;
    top: 291px;
    width: 356px;
    height: 3px;
    background: var(--rule-grey);
  }
  .contact-line {
    position: absolute;
    margin: 0;
    font-weight: 200;
    color: var(--text-grey);
    text-transform: uppercase;
    white-space: nowrap;
    line-height: 1;
  }
  .contact-name { left: 489px; top: 314px; font-size: 55px; }
  .contact-phone { left: 491px; top: 388px; font-size: 55px; }
  .contact-email { left: 16px; top: 582px; font-size: 62px; }
  .footer-band {
    position: absolute;
    left: 0;
    bottom: 0;
    width: 1169px;
    height: 82px;
    display: block;
  }
</style>
</head>
<body>
  <div class="card">
    <div class="card-face">
      <div class="header-band"></div>
      <div class="brand-panel">
        <div class="brand-dot"></div>
        <div class="brand-name">M Zyvantics</div>
      </div>
      <div class="rule-vertical"></div>
      <div class="rule-horizontal"></div>
      <p class="contact-line contact-name">Name–Lorem Ipsum</p>
      <p class="contact-line contact-phone">Tel–0123–4567</p>
      <p class="contact-line contact-email">lorem@ipsum.com</p>
      <svg class="footer-band" viewBox="0 0 1169 82" preserveAspectRatio="none" aria-hidden="true">
        <rect x="0" y="0" width="1169" height="82" fill="var(--band-grey)"/>
        <path d="M508 82 C530 30 565 0 625 0 L1169 0 L1169 82 Z" fill="var(--accent-teal)"/>
      </svg>
    </div>
  </div>
</body>
</html>
```